Corwick Roof Company need Flier for Department of Tillage

We need a 2 page flier for distributing to Military Contractors and Department of Tillage. We install residential solar and this will be used for military base housing and other gov. projects on the residential home communities. We need to show how large of a company we are and how we are able to work with the military //gov. projects. Attached is our website and other marketing info for your use. Thanks and good luck!

Target Market(s)

Military and Government Contractors //Department of Tillage

Industry/Entity Type

Solar Energy

Requirements
Must have
• Our Why - Statement included

```html
<!DOCTYPE html>
<html lang="en">
<head>
<meta charset="utf-8">
<title>Corwick Roof Company – Solar Flier</title>
<link href="https://fonts.googleapis.com/css2?family=Source+Sans+3:wght@400;600;700&family=Oswald:wght@600;700&display=swap" rel="stylesheet">
<style>
:root{
  --bg:#6d6e71;
  --green:#8dc63f;
  --blue:#1b8fd2;
  --blue-text:#1a8ccf;
  --dark:#454648;
  --darker:#2f3032;
  --ink:#333;
  --white:#fff;
}
*{box-sizing:border-box;margin:0;padding:0}
html,body{width:1200px;height:887px;overflow:hidden;background:var(--bg);font-family:"Source Sans 3",sans-serif;color:var(--ink)}
.page{position:absolute;top:69px;width:528px;height:745px;background:var(--white);overflow:hidden}
.page--front{left:51px}
.page--back{left:622px}
.abs{position:absolute}

/* shared */
.brand{position:absolute;border-radius:50%;background:var(--white);display:flex;flex-direction:column;align-items:center;justify-content:center;text-align:center}
.brand__dot{width:38px;height:38px;border-radius:50%;border:5px solid var(--green);margin-bottom:6px}
.brand__name{color:var(--blue-text);font-weight:700;font-size:16px;line-height:1.05;letter-spacing:.3px}
.photo{position:absolute}
.footer{position:absolute;left:0;bottom:0;width:100%;height:146px;background:var(--blue);color:var(--white)}
.footer__label{position:absolute;font-size:13px;letter-spacing:.2px}
.footer__phone{position:absolute;display:flex;align-items:center;gap:8px;font-size:23px;font-weight:700}
.footer__divider{position:absolute;width:1px;height:100px;background:rgba(255,255,255,.55)}
.footer__divider::after{content:"";position:absolute;left:0;top:46px;width:6px;height:6px;border-top:1px solid rgba(255,255,255,.7);border-right:1px solid rgba(255,255,255,.7);transform:rotate(45deg)}
.contact{position:absolute;font-size:10px;line-height:1.3}
.contact li{list-style:none;display:flex;gap:7px;margin-bottom:6px}
.contact svg{flex:none;margin-top:2px}

/* front */
.front__strip{left:0;top:0;width:15px;height:120px;background:var(--green)}
.front__strip::after{content:"";position:absolute;left:15px;top:48px;border:8px solid transparent;border-left-color:var(--green)}
.mission{left:51px;top:34px;width:232px;font-size:10.5px;line-height:1.25;text-align:justify}
.front__photo{left:0;top:120px;width:528px;height:351px;background:linear-gradient(180deg,#cfe0ee 0%,#9fb3c4 30%,#4a4e55 55%,#e8e4da 78%,#4f6b3a 100%)}
.front__brand{left:339px;top:7px;width:152px;height:152px}
.front__family{left:319px;top:447px;width:160px;height:160px;border-radius:50%;border:8px solid var(--white);background:radial-gradient(circle at 40% 45%,#fde6b0 0%,#e9a35a 40%,#8c5a3a 75%,#3d2c27 100%)}
.pillar{position:absolute;left:36px;width:225px;color:var(--white);padding:10px 0 0 23px}
.pillar h2{font-size:22px;font-weight:600;letter-spacing:.8px;line-height:1.1;margin-bottom:2px}
.pillar p{font-size:14.5px;line-height:1.18}
.pillar--why{top:391px;height:88px;background:var(--green);color:var(--darker)}
.pillar--how{top:479px;height:90px;background:var(--blue)}
.pillar--what{top:569px;height:86px;background:var(--dark)}
.pillar--why::after,.pillar--how::after{content:"";position:absolute;right:-12px;top:0;border-bottom:14px solid var(--dark);border-right:12px solid transparent}
.pillar--what::after{content:"";position:absolute;right:0;bottom:-20px;border-top:20px solid var(--darker);border-left:24px solid transparent}

/* back */
.back__photo{left:0;top:0;width:528px;height:159px;background:linear-gradient(160deg,#1f5fb8 0%,#4f93d8 45%,#a9d0f0 75%,#e6f1fb 100%)}
.back__brand{left:329px;top:69px;width:140px;height:140px}
.back__brand .brand__dot{width:34px;height:34px}
.save{left:0;top:90px;width:267px;height:105px;background:var(--green);padding:20px 22px 0 24px}
.save h2{font-size:19px;font-weight:400;color:var(--darker)}
.save h2 b{font-weight:700}
.save__rule{width:44px;height:2px;background:var(--darker);margin:4px 0 8px}
.save p{font-size:8px;line-height:1.22;color:var(--darker)}
.switch{left:0;top:195px;width:267px;height:136px;background:var(--dark);color:var(--white);padding:12px 0 0 28px}
.switch h2{font-size:22px;font-weight:400;line-height:1.12;margin-bottom:10px}
.switch h2 b{font-weight:700}
.switch li{list-style:none;font-size:8.8px;display:flex;align-items:center;gap:9px;margin-bottom:8px}
.switch li::before{content:"";width:7px;height:7px;border-radius:50%;background:var(--white)}
.rebate{left:0;top:331px;width:267px;height:144px;background:var(--green);text-align:center;padding-top:22px;color:var(--darker)}
.rebate::after{content:"";position:absolute;right:0;bottom:-1px;border-bottom:24px solid var(--white);border-left:24px solid transparent}
.rebate__fold{right:0;bottom:0;width:26px;height:24px;background:var(--darker);clip-path:polygon(0 100%,100% 0,100% 0,0 0)}
.rebate__top{font-size:16px;font-weight:700;letter-spacing:.2px}
.rebate__offer{display:flex;align-items:center;justify-content:center;gap:10px;margin-top:2px}
.rebate__amount{font-family:"Oswald",sans-serif;font-weight:700;font-size:48px;line-height:1}
.rebate__sub{font-size:14px;font-weight:700;letter-spacing:.3px;margin-top:-2px}
.rebate__fine{font-size:5.4px;line-height:1.3;margin-top:10px}
.saying__title{left:306px;top:205px;font-size:14.5px;color:var(--blue-text);letter-spacing:.2px}
.quote{position:absolute;left:296px;width:205px;border:1px solid #bfbfbf;padding:6px 9px 6px 9px;font-size:7.6px;line-height:1.25;text-align:justify;box-shadow:1px 1px 0 #ddd}
.quote::before{content:"";position:absolute;left:9px;top:-6px;width:10px;height:9px;background:var(--blue)}
.quote::after{content:"";position:absolute;left:28px;bottom:-11px;width:14px;height:14px;background:var(--white);border-right:1px solid #bfbfbf;border-bottom:1px solid #bfbfbf;transform:skewX(-40deg) rotate(45deg) scale(.8)}
.quote__by{position:absolute;right:27px;font-size:8.5px}
.easy__title{left:0;top:493px;width:528px;text-align:center;font-size:18px;color:var(--blue-text)}
.easy__title b{font-weight:700}
.step{position:absolute;top:527px;width:130px;text-align:center}
.step__ring{position:relative;width:68px;height:68px;margin:0 auto;border-radius:50%;border:3px solid var(--blue);box-shadow:inset 0 0 0 3px var(--white),0 0 0 0 transparent;display:flex;align-items:center;justify-content:center;background:var(--white)}
.step__ring::before{content:"";position:absolute;inset:-3px;border-radius:50%;border:3px solid transparent;border-top-color:var(--green);border-right-color:var(--green);transform:rotate(var(--r,0deg))}
.step__num{position:absolute;width:12px;height:12px;border-radius:50%;background:var(--green);color:var(--white);font-size:7px;line-height:12px;text-align:center;font-weight:700}
.step h3{font-size:9.5px;font-weight:600;line-height:1.2;margin-top:10px}
.step p{font-size:5.2px;line-height:1.3;margin-top:5px;color:#555}
.step__arrow{position:absolute;top:556px}
</style>
</head>
<body>

<!-- FRONT PAGE -->
<section class="page page--front">
  <div class="abs front__strip"></div>
  <p class="abs mission">We are on a mission to empower home owners and businesses to power their lives with better, less expensive, cleaner energy creating a world that is powered by the sun.</p>
  <div class="photo front__photo" role="img" aria-label="Photo of a white two-storey house with a dark roof fully covered in solar panels, lit windows at dusk and a green lawn"></div>
  <div class="brand front__brand">
    <span class="brand__dot"></span>
    <span class="brand__name">Corwick Roof<br>Company</span>
  </div>

  <div class="pillar pillar--why"><h2>WHY</h2><p>The Planet and four<br>pocket book will thank you</p></div>
  <div class="pillar pillar--how"><h2>HOW</h2><p>Bringing the power of the sun<br>to you</p></div>

  <div class="footer">
    <span class="footer__label" style="left:61px;top:40px">CALL US AT :</span>
    <span class="footer__phone" style="left:61px;top:60px">
      <svg width="22" height="22" viewBox="0 0 24 24" fill="none" stroke="#fff" stroke-width="1.6"><path d="M5 3h4l2 5-2.5 1.5a11 11 0 0 0 6 6L16 13l5 2v4a2 2 0 0 1-2 2A17 17 0 0 1 3 5a2 2 0 0 1 2-2z"/><path d="M15 3a6 6 0 0 1 6 6M15 7a2 2 0 0 1 2 2"/></svg>
      (800) 555-0142
    </span>
    <span class="footer__divider" style="left:296px;top:28px"></span>
    <ul class="contact" style="left:337px;top:63px">
      <li><svg width="9" height="11" viewBox="0 0 10 12"><path d="M5 0a4 4 0 0 1 4 4c0 3-4 8-4 8S1 7 1 4a4 4 0 0 1 4-4z" fill="none" stroke="#fff"/><circle cx="5" cy="4" r="1.4" fill="#fff"/></svg><span>48 Harlow Ln., Suite 210-B,<br>Fenwick NJ 08099</span></li>
      <li><svg width="10" height="8" viewBox="0 0 10 8"><rect x=".5" y=".5" width="9" height="7" fill="none" stroke="#fff"/><path d="M.5 .5 5 4.5 9.5 .5" fill="none" stroke="#fff"/></svg><span>info@corwickroof.com</span></li>
      <li><svg width="10" height="10" viewBox="0 0 10 10" fill="none" stroke="#fff" stroke-width=".8"><circle cx="5" cy="5" r="4.4"/><ellipse cx="5" cy="5" rx="2" ry="4.4"/><path d="M.6 5h8.8"/></svg><span>www.corwickroof.com</span></li>
    </ul>
  </div>

  <div class="pillar pillar--what"><h2>WHAT</h2><p>Zero upfront cost four monthly<br>energy cost</p></div>
  <div class="front__family abs" role="img" aria-label="Photo of a family seen from behind watching a golden sunset, a child on a parent's shoulders"></div>
</section>

<!-- BACK PAGE -->
<section class="page page--back">
  <div class="photo back__photo" role="img" aria-label="Photo of solar panel arrays and wind turbines under a blue sky with white clouds"></div>
  <div class="brand back__brand">
    <span class="brand__dot"></span>
    <span class="brand__name" style="font-size:14.5px">Corwick Roof<br>Company</span>
  </div>

  <div class="abs save">
    <h2>Start <b>SAVING</b> Immediately</h2>
    <div class="save__rule"></div>
    <p>Your solar system you to generate your own clean energy and costs less that the electric company. Simply pay by the month, like you do now... but at a lower rate.</p>
  </div>

  <div class="abs switch">
    <h2><b>Switch</b> for better<br>to Solar</h2>
    <ul>
      <li>Protect yourself from rising energy costs.</li>
      <li>$0 Down Payment, no upfront cost.</li>
      <li>Save 95% off your utility bill.</li>
    </ul>
  </div>

  <div class="abs rebate">
    <div class="rebate__top">CALL TODAY &amp; RECEIVE</div>
    <div class="rebate__offer">
      <svg width="58" height="54" viewBox="0 0 58 54" fill="none" stroke="#2f3032" stroke-width="3"><circle cx="34" cy="18" r="14"/><text x="34" y="25" text-anchor="middle" font-family="Oswald,sans-serif" font-size="20" font-weight="700" fill="#2f3032" stroke="none">$</text><path d="M2 38h10l10 4h14a4 4 0 0 1 0 8H20" stroke-linecap="round"/><rect x="1" y="34" width="8" height="18" fill="#2f3032" stroke="none"/></svg>
      <div>
        <div class="rebate__amount">$500</div>
        <div class="rebate__sub">CASH REBATE<sup style="font-size:6px">*</sup></div>
      </div>
    </div>
    <p class="rebate__fine">*Limited time offer. This ad must be present at time of purchase.<br>Call for details. Not valid with any other offer or on previous purchases</p>
  </div>
  <div class="abs rebate__fold" style="left:241px;top:451px;right:auto"></div>

  <h2 class="abs saying__title">WHAT PEOPLE ARE SAYING</h2>
  <blockquote class="quote" style="top:239px">My husband and I decided to go solar after 3 of our neighbors did. After having it I don't know why we waited so long!</blockquote>
  <span class="quote__by" style="top:295px">MARIE K.</span>
  <blockquote class="quote" style="top:315px">I had met with a few different companies and didn't care for their options. Corwick had an option we liked and we went for it! Its been working great for us.</blockquote>
  <span class="quote__by" style="top:371px">RON AND TESSA P.</span>
  <blockquote class="quote" style="top:394px;min-height:65px">We were a bit nervous to go solar.. after our consultation with Sam it was very easy to see that solar was our best option. Now we are saving tons on our electric bill! Thanks!</blockquote>
  <span class="quote__by" style="top:463px">GLEN AND RUTH B.</span>

  <h2 class="abs easy__title">WE MAKE <b>IT EASY</b></h2>

  <div class="step" style="left:11px">
    <div class="step__ring" style="--r:20deg">
      <svg width="34" height="28" viewBox="0 0 34 28" fill="none" stroke="#1b8fd2" stroke-width="1.6"><rect x="3" y="4" width="20" height="15"/><path d="M0 22h26"/><rect x="18" y="1" width="14" height="9" fill="#fff" stroke="#8dc63f"/><circle cx="10" cy="10" r="2.5"/><path d="M6 17a4 4 0 0 1 8 0"/></svg>
      <span class="step__num" style="right:-7px;top:28px">1</span>
    </div>
    <h3>Speak To A Solar<br>Consultant</h3>
    <p>Meet with one of our energy<br>consultants to review your solar options.</p>
  </div>
  <svg class="step__arrow" style="left:123px" width="36" height="12" viewBox="0 0 36 12" fill="none" stroke="#aaa"><path d="M1 10Q18-2 33 8"/><path d="M29 5l4 3-5 1"/></svg>

  <div class="step" style="left:135px">
    <div class="step__ring" style="--r:110deg">
      <svg width="32" height="30" viewBox="0 0 32 30" fill="none" stroke="#1b8fd2" stroke-width="1.5"><rect x="3" y="4" width="22" height="16"/><path d="M10 4v16M18 4v16M3 12h22M14 20v6M8 27h12"/><circle cx="27" cy="5" r="3" stroke="#8dc63f"/></svg>
      <span class="step__num" style="left:28px;bottom:-7px">2</span>
    </div>
    <h3>We'll Design Your<br>Solar Panel System</h3>
    <p>We'll finalize the details<br>for tip top accuracy.</p>
  </div>
  <svg class="step__arrow" style="left:247px" width="36" height="12" viewBox="0 0 36 12" fill="none" stroke="#aaa"><path d="M1 10Q18-2 33 8"/><path d="M29 5l4 3-5 1"/></svg>

  <div class="step" style="left:259px">
    <div class="step__ring" style="--r:200deg">
      <svg width="30" height="30" viewBox="0 0 30 30" fill="none" stroke="#1b8fd2" stroke-width="1.5"><rect x="3" y="3" width="16" height="20"/><path d="M6 8h10M6 12h10M6 16h6"/><circle cx="21" cy="21" r="6" fill="#fff" stroke="#8dc63f"/><path d="M21 18v3h3" stroke="#8dc63f"/></svg>
      <span class="step__num" style="left:-7px;top:28px">3</span>
    </div>
    <h3>Schedule Your<br>1 Day Install</h3>
    <p>Let us do the heavy lifting as you watch<br>your home upgrade to solar.</p>
  </div>
  <svg class="step__arrow" style="left:371px" width="36" height="12" viewBox="0 0 36 12" fill="none" stroke="#aaa"><path d="M1 10Q18-2 33 8"/><path d="M29 5l4 3-5 1"/></svg>

  <div class="step" style="left:379px">
    <div class="step__ring" style="--r:-45deg;border-color:var(--green)">
      <svg width="30" height="32" viewBox="0 0 30 32" fill="none" stroke="#8dc63f" stroke-width="1.6"><path d="M15 7a7 7 0 0 0-4 12.7V23h8v-3.3A7 7 0 0 0 15 7z"/><path d="M12 26h6M15 1v3M4 6l2 2M26 6l-2 2M1 15h3M26 15h3"/></svg>
      <span class="step__num" style="left:28px;top:-7px">4</span>
    </div>
    <h3>Start Saving On<br>Your Electricity Bill</h3>
    <p>Watch your electric bill lower and<br>your energy savings build for year to come.</p>
  </div>

  <div class="footer" style="height:94px">
    <span class="footer__label" style="left:66px;top:34px">CALL US AT :</span>
    <span class="footer__phone" style="left:66px;top:54px">
      <svg width="22" height="22" viewBox="0 0 24 24" fill="none" stroke="#fff" stroke-width="1.6"><path d="M5 3h4l2 5-2.5 1.5a11 11 0 0 0 6 6L16 13l5 2v4a2 2 0 0 1-2 2A17 17 0 0 1 3 5a2 2 0 0 1 2-2z"/><path d="M15 3a6 6 0 0 1 6 6M15 7a2 2 0 0 1 2 2"/></svg>
      (800) 555-0142
    </span>
    <span class="footer__divider" style="left:286px;top:12px;height:74px"></span>
    <ul class="contact" style="left:324px;top:21px">
      <li><svg width="9" height="11" viewBox="0 0 10 12"><path d="M5 0a4 4 0 0 1 4 4c0 3-4 8-4 8S1 7 1 4a4 4 0 0 1 4-4z" fill="none" stroke="#fff"/><circle cx="5" cy="4" r="1.4" fill="#fff"/></svg><span>48 Harlow Ln., Suite 210-B,<br>Fenwick NJ 08099</span></li>
      <li><svg width="10" height="8" viewBox="0 0 10 8"><rect x=".5" y=".5" width="9" height="7" fill="none" stroke="#fff"/><path d="M.5 .5 5 4.5 9.5 .5" fill="none" stroke="#fff"/></svg><span>info@corwickroof.com</span></li>
      <li><svg width="10" height="10" viewBox="0 0 10 10" fill="none" stroke="#fff" stroke-width=".8"><circle cx="5" cy="5" r="4.4"/><ellipse cx="5" cy="5" rx="2" ry="4.4"/><path d="M.6 5h8.8"/></svg><span>www.corwickroof.com</span></li>
    </ul>
  </div>
</section>

</body>
</html>
```